CV for an Urgent Care Trade Association Executive search candidate in need of competitive CV refresh

I need a CV refresh to be able to show marketability and skill in a competitive Executive search. I would like to see designs that highlight my skill and ability to hopefully put me in the front running for position.

Industry/Entity Type

Medical/Urgent Care

Requirements
Must have
• CV template
Nice to have
• Nice to have a CV template to be able to add my personal info into

```html
<!DOCTYPE html>
<html lang="en">
<head>
<meta charset="utf-8">
<title>Marisol Thornbury — CV and Cover Letter</title>
<link href="https://fonts.googleapis.com/css2?family=Lato:wght@300;400;700&display=swap" rel="stylesheet">
<style>
  :root{
    --backdrop:#b2b8b8;
    --paper:#ffffff;
    --ink:#3b3b3b;
    --ink-soft:#555555;
    --ink-muted:#737373;
    --rule:#dcdcdc;
    --rule-dark:#8a8a8a;
    --bar-track:#d6d6d6;
    --bar-fill:#4a4a4a;
    --crimson:#a8002f;
    --ember:#dd4b22;
    --amber:#fbad16;
  }
  *{box-sizing:border-box;margin:0;padding:0}
  html,body{width:1200px;height:739px;overflow:hidden}
  body{background:var(--backdrop);font-family:'Lato',sans-serif;color:var(--ink);position:relative}

  .sheet{position:absolute;top:69px;width:419px;height:587px;background:var(--paper);
    box-shadow:0 14px 18px -10px rgba(0,0,0,.35)}
  .sheet--cv{left:144px}
  .sheet--letter{left:632px}
  .sheet > *{position:absolute}

  .accent-tab{left:362px;top:0;width:21px;height:65px;
    background:linear-gradient(180deg,var(--ember) 0%,var(--amber) 40%,var(--ember) 72%,var(--crimson) 100%)}
  .footer-band{left:0;bottom:0;width:100%;height:12px;
    background:linear-gradient(90deg,var(--crimson) 0%,var(--ember) 25%,var(--amber) 50%,var(--ember) 75%,var(--crimson) 100%)}

  .name{left:35px;top:34px;font-weight:300;font-size:33px;line-height:27px;letter-spacing:.5px;color:var(--ink)}
  .role{left:275px;top:77px;font-size:9.6px;letter-spacing:1.9px;color:var(--ink-soft);font-weight:400}
  .header-rule{left:34px;top:101px;width:349px;height:1px;background:var(--rule)}
  .header-rule::before,.header-rule::after{content:"";position:absolute;top:0;width:14px;height:1px;background:var(--rule-dark)}
  .header-rule::before{left:0}
  .header-rule::after{left:241px}

  .section-title{font-size:9.4px;font-weight:700;color:var(--ink);letter-spacing:.1px}
  .section-title::after{content:"";position:absolute;left:0;top:13px;width:100%;height:1px;background:var(--rule)}
  .section-title span{position:absolute;left:0;top:13px;width:14px;height:1px;background:var(--rule-dark);z-index:1}

  .col-divider{top:131px;width:1px;height:82px;background:var(--rule)}

  .about-text{left:35px;top:155px;width:100px;font-size:5.4px;line-height:8.2px;color:var(--ink-muted)}
  .degree{left:165px;width:95px}
  .degree h3{font-size:7.6px;font-weight:400;color:var(--ink);line-height:9px}
  .degree p{font-size:5.8px;color:var(--ink-soft);line-height:8.5px}

  .contact-address{left:283px;top:155px;font-size:6px;line-height:7.6px;color:var(--ink-soft)}
  .contact-line{left:283px;display:flex;align-items:center;gap:4px;font-size:6px;color:var(--ink-soft)}
  .contact-line svg{width:6px;height:6px;fill:none;stroke:var(--ink-soft);stroke-width:1.2}

  .timeline{left:125px;top:275px;width:1px;height:189px;background:var(--rule)}
  .job{left:0;width:419px;height:69px}
  .job > *{position:absolute}
  .job-dates{left:35px;top:0;font-size:5.6px;color:var(--ink-soft)}
  .job-title{left:35px;top:8px;font-size:7px;color:var(--ink)}
  .job-location{left:35px;top:18px;font-size:5.6px;color:var(--ink-soft)}
  .job-dot{left:123px;top:1px;width:5px;height:5px;border-radius:50%;background:var(--ink-soft)}
  .company{left:142px;top:0;font-size:5.8px;letter-spacing:.2px;color:var(--ink)}
  .job-desc{left:143px;top:8px;width:240px;font-size:5.6px;line-height:8.8px;color:var(--ink-muted)}
  .job-point{left:150px;top:37px;width:205px;font-size:5.6px;line-height:8.3px;color:var(--ink-muted)}
  .job-point::before{content:"";position:absolute;left:-7px;top:3px;width:2.6px;height:2.6px;border-radius:50%;background:var(--ink-soft)}

  .skill{display:flex;align-items:center;font-size:6.2px;color:var(--ink)}
  .skill-name{width:77px}
  .skill-bar{width:56px;height:2px;background:var(--bar-track);position:relative}
  .skill-bar i{position:absolute;left:0;top:0;height:2px;background:var(--bar-fill)}

  .letter-small{font-size:5.4px;color:var(--ink-soft)}
  .letter-body{left:35px;width:344px;font-size:5.5px;line-height:8.8px;color:var(--ink-muted)}
</style>
</head>
<body>

<!-- Curriculum vitae -->
<section class="sheet sheet--cv">
  <div class="accent-tab"></div>
  <h1 class="name">MARISOL<br>THORNBURY</h1>
  <p class="role">CREATIVE DIRECTOR</p>
  <div class="header-rule"></div>

  <h2 class="section-title" style="left:34px;top:129px;width:88px">ABOUT ME<span></span></h2>
  <p class="about-text">At vero eos et accusamus et iusto odio dignissimos ducimus blanditiis praesentium voluptatum deleni atque corrupti qu dolores et quas molestias excepturi sint occaecati cupiditate non provident animi, deleni atcorrupti qu dolores et quas.</p>
  <div class="col-divider" style="left:151px"></div>

  <h2 class="section-title" style="left:165px;top:129px;width:89px">EDUCATION<span></span></h2>
  <div class="degree" style="top:154px"><h3>Bachelor of Creative Arts</h3><p>Name of University / Location</p><p>2010 - 2012</p></div>
  <div class="degree" style="top:187px"><h3>Master Communication</h3><p>Name of University / Location</p><p>2013 - 2014</p></div>
  <div class="col-divider" style="left:268px"></div>

  <h2 class="section-title" style="left:283px;top:129px;width:88px">CONTACT<span></span></h2>
  <p class="contact-address">Your address here, 1234,<br>location name</p>
  <p class="contact-line" style="top:180px"><svg viewBox="0 0 10 10"><path d="M2 1l2 0 1 2.5-1.3 1a6 6 0 0 0 2.8 2.8l1-1.3L10 7v2c-4.5.3-8.3-3.5-8-8z" fill="#555" stroke="none"/></svg>000 1234 56789</p>
  <p class="contact-line" style="top:190px"><svg viewBox="0 0 10 10"><rect x="0.8" y="2" width="8.4" height="6"/><path d="M1 2.3l4 3.2 4-3.2"/></svg>yourmail@email.com</p>
  <p class="contact-line" style="top:201px"><svg viewBox="0 0 10 10"><circle cx="5" cy="5" r="4"/><ellipse cx="5" cy="5" rx="1.8" ry="4"/><path d="M1 5h8M1.6 3h6.8M1.6 7h6.8"/></svg>www.yourwebsite.com</p>

  <h2 class="section-title" style="left:34px;top:240px;width:349px">WORK EXPERIENCE<span></span></h2>
  <div class="timeline"></div>

  <article class="job" style="top:274px">
    <p class="job-dates">2012 - 2014</p><p class="job-title">Your Job Title Goes Here</p><p class="job-location">Location Here</p>
    <span class="job-dot"></span><p class="company">COMPANY NAME</p>
    <p class="job-desc">Lorem ipsum dolor sit amet, consectetur adipiscing elit, sed do eiusm tempor incididunt ut labore et dolore magna aliqua. Ut enim ad minim venia nos exercitation ullamco laboris nisi ut aliquip onsequat.</p>
    <p class="job-point">It is a long established fact that a reader will be distracted by the readable content of a page when looking at its layout.</p>
  </article>
  <article class="job" style="top:343px">
    <p class="job-dates">2012 - 2014</p><p class="job-title">Your Job Title Goes Here</p><p class="job-location">Location Here</p>
    <span class="job-dot"></span><p class="company">COMPANY NAME</p>
    <p class="job-desc">Lorem ipsum dolor sit amet, consectetur adipiscing elit, sed do eiusm tempor incididunt ut labore et dolore magna aliqua. Ut enim ad minim venia nos exercitation ullamco laboris nisi ut aliquip onsequat.</p>
    <p class="job-point">It is a long established fact that a reader will be distracted by the readable content of a page when looking at its layout.</p>
  </article>
  <article class="job" style="top:411px">
    <p class="job-dates">2012 - 2014</p><p class="job-title">Your Job Title Goes Here</p><p class="job-location">Location Here</p>
    <span class="job-dot"></span><p class="company">COMPANY NAME</p>
    <p class="job-desc">Lorem ipsum dolor sit amet, consectetur adipiscing elit, sed do eiusm tempor incididunt ut labore et dolore magna aliqua. Ut enim ad minim venia nos exercitation ullamco laboris nisi ut aliquip onsequat.</p>
    <p class="job-point">It is a long established fact that a reader will be distracted by the readable content of a page when looking at its layout.</p>
  </article>

  <h2 class="section-title" style="left:34px;top:488px;width:349px">EXPERTISE<span></span></h2>
  <p class="skill" style="left:35px;top:516px"><span class="skill-name">Clinic Ops Suite</span><span class="skill-bar"><i style="width:69%"></i></span></p>
  <p class="skill" style="left:35px;top:528px"><span class="skill-name">Layout Studio</span><span class="skill-bar" style="width:54px"><i style="width:91%"></i></span></p>
  <p class="skill" style="left:35px;top:539px"><span class="skill-name">Sheetwise Data</span><span class="skill-bar" style="width:54px"><i style="width:71%"></i></span></p>
  <p class="skill" style="left:210px;top:516px"><span class="skill-name">Vector Draft</span><span class="skill-bar" style="width:54px"><i style="width:93%"></i></span></p>
  <p class="skill" style="left:210px;top:527px"><span class="skill-name">Motion Forge</span><span class="skill-bar" style="width:54px"><i style="width:70%"></i></span></p>
  <p class="skill" style="left:210px;top:539px"><span class="skill-name">Sheetwise Data</span><span class="skill-bar" style="width:54px"><i style="width:85%"></i></span></p>

  <div class="footer-band"></div>
</section>

<!-- Cover letter -->
<section class="sheet sheet--letter">
  <div class="accent-tab"></div>
  <h1 class="name">MARISOL<br>THORNBURY</h1>
  <p class="role">CREATIVE DIRECTOR</p>
  <div class="header-rule"></div>

  <h2 class="section-title" style="left:34px;top:129px;width:88px">ABOUT ME<span></span></h2>
  <p class="about-text">At vero eos et accusamus et iusto odio dignissimos ducimus blanditiis praesentium voluptatum deleni atque corrupti qu dolores et quas molestias excepturi sint occaecati cupiditate non provident animi, deleni atcorrupti qu dolores et quas.</p>
  <div class="col-divider" style="left:151px"></div>

  <h2 class="section-title" style="left:165px;top:129px;width:89px">EDUCATION<span></span></h2>
  <div class="degree" style="top:154px"><h3>Bachelor of Creative Arts</h3><p>Name of University / Location</p><p>2010 - 2012</p></div>
  <div class="degree" style="top:187px"><h3>Master Communication</h3><p>Name of University / Location</p><p>2013 - 2014</p></div>
  <div class="col-divider" style="left:268px"></div>

  <h2 class="section-title" style="left:283px;top:129px;width:88px">CONTACT<span></span></h2>
  <p class="contact-address">Your address here, 1234,<br>location name, UK</p>
  <p class="contact-line" style="top:180px"><svg viewBox="0 0 10 10"><path d="M2 1l2 0 1 2.5-1.3 1a6 6 0 0 0 2.8 2.8l1-1.3L10 7v2c-4.5.3-8.3-3.5-8-8z" fill="#555" stroke="none"/></svg>000 1234 56789</p>
  <p class="contact-line" style="top:190px"><svg viewBox="0 0 10 10"><rect x="0.8" y="2" width="8.4" height="6"/><path d="M1 2.3l4 3.2 4-3.2"/></svg>yourmail@email.com</p>
  <p class="contact-line" style="top:201px"><svg viewBox="0 0 10 10"><circle cx="5" cy="5" r="4"/><ellipse cx="5" cy="5" rx="1.8" ry="4"/><path d="M1 5h8M1.6 3h6.8M1.6 7h6.8"/></svg>www.yourwebsite.com</p>

  <h2 class="section-title" style="left:34px;top:240px;width:349px">COVER LETTER<span></span></h2>

  <p style="left:35px;top:267px;font-size:7px">To</p>
  <p style="left:35px;top:279px;font-size:7px">John Doe</p>
  <p class="letter-small" style="left:35px;top:289px">Position</p>
  <p class="letter-small" style="left:35px;top:297px">Your Address Name,123. State, Country.</p>
  <p class="letter-small" style="right:37px;top:297px">Date: 15 september 2025</p>

  <p style="left:35px;top:327px;font-size:7px;font-weight:700;color:var(--ink-soft)">Dear Sir / Madam</p>
  <p class="letter-body" style="top:344px">Lorem ipsum dolor sit amet, consec adipiscing elit, sed do eiusm tempor incididunt ut labore et dolore magna aliqua. Ut enim ad minim venia nostrud exercitation.It is a long established fact that a reader will be distracted by the readable content of a page when. Lorem Ipsum is simply dummy text of the printing and typesetting industry. Lorem Ipsum has been tindustry's standard dummy text ever since the 1500s, when an unknown printer took a galley of type and scrambled it to make a type specimen book. It has survived not only fivcenturies, but also the leap into electronic typesetting, remaining essentially unchanged.</p>
  <p class="letter-body" style="top:397px">It was popularised in the 1960s with the release of Lettrafax sheets containing Lorem Ipsum passages, and more recently with desktop publishing software like Pagewright Studio including versions of Lorem Ipsum.There are many variations of passages of Lorem Ipsu available, but the majority have suffered alteration in some form, by injected humour, or randomised hidden in the middle of text.</p>
  <p class="letter-body" style="top:441px">All the Lorem Ipsum generators on the Internet tend to repeat predefined chunks took a galley of type and scrambled it to make a type specimen book. It has survived not only five centuries, as necessary, making this the first true generator on the Internet.Content here, content here', making it look like readable English. Many desktop publishing packages and web page editors now use Lorem Ipsum</p>

  <p style="left:35px;top:516px;font-size:4.6px;color:var(--ink-soft)">Sincerely</p>
  <p style="left:35px;top:523px;font-size:5.6px;color:var(--ink)">Your Name</p>

  <div class="footer-band"></div>
</section>

</body>
</html>
```